Heron Freightlines needs Bussiness cards!

Our new trucking company needs business cards!
We need the same design with two different names and emails, everything else it's the same.
I have included our original logo so we can use it for the design.
Note: the logo to be used is the o e with the buffalo on the right side, next to the letters H and F.

Target Market(s)

Trucking, refrigerated transportation, freight

Industry/Entity Type

Business

Contact Information for Business Card

Card #1:
Marcus Tellwright
marcustellwright@heronfreightlines.example
1-844-555-0193
(956)555-0178
3817 W. Tarrow Ave.
Pharr, TX 78599
www.heronfreightlines.example

Card#2:
Orla Brennick
orla@heronfreightlines.example
1-844-555-0193
(956)555-0178
3817 W. Tarrow Ave.
Pharr, TX 78599
www.heronfreightlines.example

Font styles to use
Sans Serif

Colors
0655a3
ec1f27
ffffff

Requirements
Must have
• our logo
Nice to have
• roads on background,

```html
<!DOCTYPE html>
<html lang="en">
<head>
<meta charset="utf-8">
<title>Heron Freightlines — Business Cards</title>
<link href="https://fonts.googleapis.com/css2?family=Open+Sans:wght@400;600;800&display=swap" rel="stylesheet">
<style>
  :root {
    --page-bg: #e6e4e0;
    --slate: #46566f;
    --slate-dark: #3a4860;
    --slate-light: #5d6d88;
    --stripe-red: #c65760;
    --paper: #ffffff;
    --ink-navy: #3d4c66;
    --ink-light: #eef1f6;
  }
  * { box-sizing: border-box; margin: 0; padding: 0; }
  html, body {
    width: 1200px; height: 1062px; overflow: hidden;
    background: var(--page-bg);
    font-family: "Open Sans", Arial, sans-serif;
  }
  .sheet {
    position: relative; width: 1200px; height: 1062px;
    display: flex; flex-direction: column; align-items: center;
    justify-content: center; gap: 44px;
  }
  .card {
    position: relative; width: 840px; height: 480px; overflow: hidden;
    box-shadow: 0 10px 28px rgba(40, 40, 40, 0.22);
  }

  /* Front */
  .card-front {
    background: linear-gradient(135deg, var(--slate-light) 0%, var(--slate) 45%, var(--slate-dark) 100%);
  }
  .front-emblem-area {
    position: absolute; left: 40px; top: 40px; width: 430px; height: 400px;
    border-radius: 50%;
    background: radial-gradient(ellipse at 50% 50%, rgba(170, 186, 210, 0.35) 0%, rgba(170, 186, 210, 0.08) 70%, rgba(170, 186, 210, 0) 100%);
  }
  .front-wordmark {
    position: absolute; right: 70px; top: 50%; transform: translateY(-50%);
    color: var(--paper); font-weight: 800; font-size: 52px; line-height: 1.05;
    text-align: right; letter-spacing: -0.5px;
  }

  /* Back */
  .card-back { background: var(--paper); }
  .back-shapes { position: absolute; inset: 0; }
  .back-wordmark {
    position: absolute; left: 300px; top: 60px; width: 480px;
    display: flex; align-items: center; gap: 16px;
    color: var(--ink-navy); font-weight: 800; font-size: 44px; line-height: 1.05;
  }
  .wordmark-dot {
    flex: none; width: 40px; height: 40px; border-radius: 50%;
    background: var(--stripe-red);
  }
  .holder-name {
    position: absolute; right: 40px; top: 226px;
    color: var(--ink-navy); font-weight: 600; font-size: 22px; line-height: 30px;
  }
  .contact-list {
    position: absolute; left: 40px; right: 40px; top: 310px;
    list-style: none; color: var(--ink-light); font-size: 17px; line-height: 25px;
  }
  .contact-list li { display: flex; align-items: center; gap: 10px; white-space: nowrap; }
  .contact-icon {
    flex: none; width: 20px; height: 20px; border-radius: 4px;
    background: rgba(255, 255, 255, 0.85);
  }
  .contact-icon svg { display: block; width: 20px; height: 20px; }
</style>
</head>
<body>
<main class="sheet">

  <section class="card card-front" aria-label="Card front">
    <div class="front-emblem-area" role="img" aria-label="Large faint bison head illustration watermark"></div>
    <div class="front-wordmark">Heron<br>Freightlines</div>
  </section>

  <section class="card card-back" aria-label="Card back">
    <svg class="back-shapes" viewBox="0 0 840 480" aria-hidden="true">
      <polygon points="0,0 60,0 60,250 470,250 520,290 840,290 840,480 0,480" fill="var(--slate)"/>
      <polygon points="60,0 78,0 78,232 478,232 528,272 840,272 840,290 520,290 470,250 60,250" fill="var(--stripe-red)"/>
    </svg>

    <div class="back-wordmark">
      <span class="wordmark-dot"></span>
      <span>Heron<br>Freightlines</span>
    </div>

    <div class="holder-name">Marcus Tellwright</div>

    <ul class="contact-list">
      <li>
        <span class="contact-icon"><svg viewBox="0 0 20 20"><path d="M10 3.5a4.5 4.5 0 0 0-4.5 4.5c0 3.5 4.5 8.5 4.5 8.5s4.5-5 4.5-8.5A4.5 4.5 0 0 0 10 3.5z" fill="var(--slate)"/><circle cx="10" cy="8" r="1.6" fill="#fff"/></svg></span>
        <span>3817 W. Tarrow Ave., Pharr, TX 78599</span>
      </li>
      <li>
        <span class="contact-icon"><svg viewBox="0 0 20 20"><path d="M6 4l3 3-1.5 1.5a8 8 0 0 0 4 4L13 11l3 3-2 2C9 16 4 11 4 6z" fill="var(--slate)"/></svg></span>
        <span>(956)555-0178</span>
      </li>
      <li>
        <span class="contact-icon"><svg viewBox="0 0 20 20"><rect x="6.5" y="3.5" width="7" height="13" rx="1.2" fill="none" stroke="var(--slate)" stroke-width="1.6"/><circle cx="10" cy="14" r="0.9" fill="var(--slate)"/></svg></span>
        <span>1-844-555-0193</span>
      </li>
      <li>
        <span class="contact-icon"><svg viewBox="0 0 20 20"><text x="10" y="14.5" text-anchor="middle" font-family="Open Sans, Arial, sans-serif" font-weight="800" font-size="13" fill="var(--slate)">@</text></svg></span>
        <span>marcustellwright@heronfreightlines.example</span>
      </li>
      <li>
        <span class="contact-icon"><svg viewBox="0 0 20 20"><circle cx="10" cy="10" r="6" fill="none" stroke="var(--slate)" stroke-width="1.6"/><path d="M4 10h12M10 4c-3 3.5-3 8.5 0 12M10 4c3 3.5 3 8.5 0 12" fill="none" stroke="var(--slate)" stroke-width="1.2"/></svg></span>
        <span>www.heronfreightlines.example</span>
      </li>
    </ul>
  </section>

</main>
</body>
</html>
```